Radiology Department needs a series of 3 facebook posts - similar design

We need a series of 3 posts for our facebook page, each one presenting the activity of one of 3 physicians.
The main design elements can be the same, the only thing that will change between posts will be the field of activity and name of the physician and the representative image of its activity.
If needed the design elements can be slightly different between posts for better adjustment to the representative images.
You can find as an attachment:
- Manual of institutional identity of the Hospital (Vendra Clinis)
- Our facebook cover page
- Our department video
- The representative images for each post, identified with the name of each physician
- The Institutional identity manual with the logo of "Ravessa Medical School" - just for Dr Tomé Vasconde post.
So, each one of the three posts should state the name and field of activity of each physician, including somehow the corresponding representative image, and should have background innovative design elements.
Post 1:
Name of the physician: Prof. Doutor Rui Bastardo
Field of activity: Imagiologia Reumatológica e do Sistema Músculo-Esquelético
Image as an attachment
Post 2:
Name of the physician: Prof.ª Doutora Inês Furtado
Field of activity: Imagiologia Cardíaca
Image as an attachment
Post 3:
Name of the physician: Dr. Tomé Sousel
Field of activity: Tese de Doutoramento em Curso - Identificação da Lesão Cartilagínea Precoce. Com orientação do Prof. Doutor Rui Bastardo e Prof.ª Doutora Clara Sofia Pimentel.
Image as an attachment
Just for Dr Tomé Sousel, the logo of Ravessa Medical School should also be included (please check the corresponding institutional identity manual that was just added in documents).
Updates

Just for Dr Tomé Vasconde, the logo of Ravessa Medical School should also be included (please check the corresponding institutional identity manual that was just added in documents).

Please note that we are just looking for 3 facebook POSTS, not facebook cover page, thanks.

Please kindly note that we are looking for facebook POST and NOT facebook cover page.

Target Market(s)

General Population

Industry/Entity Type

Health

Font styles to use
Other font styles liked:
• Check manual of institutional identity and try to approach if appropriate

Requirements
Must have
• Check project description.
Nice to have
• If the designer finds appropriate, the logo of the Hospital would be nice in all the three posts, the most simple one just stating "VendraClinis" - please check the attached manual of institutional identity

```html
<!DOCTYPE html>
<html lang="pt">
<head>
<meta charset="utf-8">
<title>VendraClinis – Facebook Posts</title>
<link href="https://fonts.googleapis.com/css2?family=Nunito+Sans:wght@400;700;800;900&display=swap" rel="stylesheet">
<style>
  :root {
    --board: #c8c8c8;
    --teal: #00616f;
    --teal-dark: #0b4f5c;
    --orange: #f7a823;
    --white: #ffffff;
    --ink: #1d1d1d;
    --black: #050505;
  }
  * { margin: 0; padding: 0; box-sizing: border-box; }
  html, body { width: 1200px; height: 465px; overflow: hidden; background: var(--board); }
  body { font-family: "Nunito Sans", Arial, sans-serif; position: relative; }

  .post-label {
    position: absolute; top: 66px;
    font-size: 11px; font-weight: 700; color: var(--ink); letter-spacing: .3px;
  }
  .post {
    position: absolute; top: 95px; width: 336px; height: 336px;
    background: var(--black); overflow: hidden;
    box-shadow: 0 1px 3px rgba(0,0,0,.18);
  }
  .post--one { left: 53px; }
  .post--two { left: 429px; }
  .post--three { left: 806px; }

  .visual { position: absolute; }
  .visual--hands {
    left: 130px; top: 0; width: 206px; height: 220px;
    background: radial-gradient(ellipse at 45% 45%, #9a9a9a 0%, #5d5d5d 35%, #1b1b1b 70%, var(--black) 100%);
  }
  .visual--heart {
    left: 140px; top: 8px; width: 190px; height: 200px;
    background: radial-gradient(ellipse at 45% 60%, #7a1e16 0%, #5a140f 40%, #2a0806 65%, var(--black) 85%);
  }
  .visual--cartilage {
    left: 86px; top: 0; width: 250px; height: 230px;
    background: radial-gradient(ellipse at 60% 45%, #1232c8 0%, #0d2ab8 45%, #0a1f8a 75%, #0a1550 100%);
  }

  .frame { position: absolute; inset: 0; width: 336px; height: 336px; }

  .brand {
    position: absolute; left: 11px; top: 13px;
    display: flex; align-items: center; gap: 5px;
  }
  .brand__dot { width: 26px; height: 26px; border-radius: 50%; background: var(--teal); }
  .brand__name { font-size: 16px; font-weight: 700; color: var(--teal); letter-spacing: .1px; }

  .physician {
    position: absolute; left: 50%; transform: translateX(-50%);
    background: var(--orange); border-radius: 11px;
    padding: 2px 10px; white-space: nowrap;
    font-size: 11px; color: var(--teal-dark); font-weight: 400;
  }
  .physician strong { font-weight: 800; }

  .headline {
    position: absolute; left: 0; right: 0; text-align: center;
    color: var(--white); font-weight: 900; line-height: .98; letter-spacing: -.5px;
  }
  .headline--rheuma { top: 244px; font-size: 24px; }
  .headline--cardio { top: 249px; font-size: 32px; letter-spacing: -1px; line-height: 1.05; }
  .headline--cardio .headline__big { font-size: 38px; }
  .headline--thesis { top: 232px; font-size: 19px; }

  .subline {
    position: absolute; left: 0; right: 0; text-align: center; color: var(--white);
  }
  .subline--rheuma { top: 300px; font-size: 16px; font-weight: 700; }
  .subline--thesis { top: 279px; font-size: 10px; font-weight: 800; letter-spacing: .2px; }

  .partner {
    position: absolute; left: 15px; top: 304px;
    display: flex; align-items: center; gap: 4px;
  }
  .partner__square { width: 12px; height: 12px; background: var(--white); }
  .partner__name { font-size: 8px; font-weight: 800; color: var(--white); letter-spacing: .2px; line-height: 1.05; }

  .advisors {
    position: absolute; left: 129px; top: 304px;
    font-size: 8px; line-height: 1.15; color: var(--white);
  }
  .advisors strong { color: var(--orange); font-weight: 700; }
</style>
</head>
<body>

  <p class="post-label" style="left:52px">FB POST 1</p>
  <p class="post-label" style="left:428px">FB POST 2</p>
  <p class="post-label" style="left:806px">FB POST 3</p>

  <section class="post post--one">
    <div class="visual visual--hands" role="img" aria-label="Angiographic scan of both hands showing blood vessels"></div>
    <svg class="frame" viewBox="0 0 336 336">
      <path d="M0 0 H166 Q120 62 0 66 Z" fill="var(--white)"/>
      <path d="M166 0 Q120 62 0 66 V71 Q126 67 172 0 Z" fill="var(--orange)"/>
      <path d="M0 242 Q168 200 336 248 V336 H0 Z" fill="var(--orange)"/>
      <path d="M0 250 Q168 212 336 256 V336 H0 Z" fill="var(--teal)"/>
    </svg>
    <div class="brand"><span class="brand__dot"></span><span class="brand__name">VendraClinis</span></div>
    <p class="physician" style="top:212px">Physician: <strong>Prof. Doutor Rui Bastardo</strong></p>
    <h2 class="headline headline--rheuma">IMAGIOLOGIA<br>REUMATOLÓGICA</h2>
    <p class="subline subline--rheuma">e do Sistema Músculo-Esquelético</p>
  </section>

  <section class="post post--two">
    <div class="visual visual--heart" role="img" aria-label="3D rendering of the heart with coronary arteries"></div>
    <svg class="frame" viewBox="0 0 336 336">
      <path d="M0 0 H166 Q120 62 0 66 Z" fill="var(--white)"/>
      <path d="M166 0 Q120 62 0 66 V71 Q126 67 172 0 Z" fill="var(--orange)"/>
      <path d="M0 242 Q168 200 336 248 V336 H0 Z" fill="var(--orange)"/>
      <path d="M0 250 Q168 212 336 256 V336 H0 Z" fill="var(--teal)"/>
    </svg>
    <div class="brand"><span class="brand__dot"></span><span class="brand__name">VendraClinis</span></div>
    <p class="physician" style="top:212px">Physician: <strong>Prof.ª Doutora Inês Furtado</strong></p>
    <h2 class="headline headline--cardio">IMAGIOLOGIA<br><span class="headline__big">CARDÍACA</span></h2>
  </section>

  <section class="post post--three">
    <div class="visual visual--cartilage" role="img" aria-label="Colour-mapped MRI scan of knee cartilage"></div>
    <svg class="frame" viewBox="0 0 336 336">
      <path d="M0 0 H166 Q120 62 0 66 Z" fill="var(--white)"/>
      <path d="M166 0 Q120 62 0 66 V71 Q126 67 172 0 Z" fill="var(--orange)"/>
      <path d="M0 228 Q168 186 336 232 V336 H0 Z" fill="var(--orange)"/>
      <path d="M0 236 Q168 198 336 240 V336 H0 Z" fill="var(--teal)"/>
    </svg>
    <div class="brand"><span class="brand__dot"></span><span class="brand__name">VendraClinis</span></div>
    <p class="physician" style="top:199px;font-size:13px;padding:2px 18px">Physician: <strong>Dr. Tomé Sousel</strong></p>
    <h2 class="headline headline--thesis">TESE DE DOUTORAMENTO<br>EM CURSO</h2>
    <p class="subline subline--thesis">IDENTIFICAÇÃO DA LESÃO CARTILAGÍNEA PRECOCE.</p>
    <div class="partner"><span class="partner__square"></span><span class="partner__name">RAVESSA<br>MEDICAL SCHOOL</span></div>
    <p class="advisors">Com orientação do <strong>Prof. Doutor Rui Bastardo</strong><br><strong>e Prof.ª Doutora Clara Sofia Pimentel.</strong></p>
  </section>

</body>
</html>
```